Technical audit needs a report template

As our company runs various technical audits, we also provide findings on paper, online or in Powerpoint. For this reason we need an identity pack, which includes business cards, complimentary cards, letterhead and the likes.

Who would be up to create this stationery pack for us? We hope to receive a style for these documents, that look professional and can be easily extended.
Updates

Project Deadline Extended Reason: I would like to provide the opportunity to friended designers to submit their designs too! Added Sunday, October 9, 2016

Target Market(s)

Start-ups, scale-ups and investors

Industry/Entity Type

Investment

Contact Information for Business Card

Street: Lindenhoutkade 42
Postcode: 3617KW
City: Utrecht
Country: The Netherlands
Phone: +31 302849516
Cell Phone: +31 6 58193074
email: jeroen@vexomari.example
website: https://vexomari.example

Requirements
Must have
• I don't have inspiration, should just be a slick design based on the logo provided.
Nice to have
• Logo could be on the back of the card?
Should not have
• Should not use different colours then the logo, or at least fit the colour scheme.

```html
<!DOCTYPE html>
<html lang="en">
<head>
<meta charset="utf-8">
<title>Vexomari business card</title>
<link href="https://fonts.googleapis.com/css2?family=Open+Sans:wght@400;600&display=swap" rel="stylesheet">
<style>
  :root {
    --backdrop: #d9d6d3;
    --card: #141516;
    --card-edge: #1d1e20;
    --accent: #2fa9d6;
    --text: #e9eaeb;
    --muted: #8a8c8f;
    --rule: #4a4c4f;
  }
  * { box-sizing: border-box; margin: 0; padding: 0; }
  html, body { width: 1200px; height: 864px; overflow: hidden; }
  body {
    background: var(--backdrop);
    font-family: "Open Sans", Arial, sans-serif;
    position: relative;
  }
  .card {
    position: absolute;
    width: 540px;
    height: 310px;
    background: linear-gradient(135deg, var(--card-edge), var(--card));
    box-shadow: 0 10px 30px rgba(0,0,0,.35);
  }
  .card--back { left: 40px; top: 120px; }
  .card--front { left: 620px; top: 430px; }

  /* back */
  .back-mark {
    position: absolute; left: 0; right: 0; top: 90px;
    display: flex; align-items: center; justify-content: center; gap: 14px;
  }
  .back-mark__square { width: 34px; height: 34px; border: 5px solid #3a3c3f; }
  .back-mark__name { font-size: 44px; font-weight: 600; color: #3a3c3f; letter-spacing: 1px; }
  .back-web {
    position: absolute; left: 0; right: 0; top: 205px;
    text-align: center; font-size: 13px; letter-spacing: 5px; color: var(--muted);
  }

  /* front */
  .brand {
    position: absolute; left: 34px; top: 128px;
    display: flex; align-items: center; gap: 12px;
  }
  .brand__square { width: 40px; height: 40px; background: var(--accent); }
  .brand__name { font-size: 34px; font-weight: 600; color: var(--accent); }
  .divider {
    position: absolute; left: 272px; top: 48px; width: 1px; height: 214px;
    background: linear-gradient(var(--card), var(--rule) 30%, var(--rule) 70%, var(--card));
  }
  .contact { position: absolute; left: 298px; top: 52px; color: var(--text); font-size: 13px; line-height: 1.55; }
  .contact__name { font-size: 18px; font-weight: 600; color: var(--accent); line-height: 1.2; }
  .contact__role { font-size: 14px; margin-bottom: 10px; }
  .contact__address { margin-bottom: 4px; }
  .contact__line { display: flex; align-items: center; gap: 8px; }
  .contact__line svg { width: 12px; height: 12px; fill: var(--accent); flex: none; }
</style>
</head>
<body>
  <section class="card card--back">
    <div class="back-mark">
      <span class="back-mark__square"></span>
      <span class="back-mark__name">Vexomari</span>
    </div>
    <p class="back-web">vexomari.example</p>
  </section>

  <section class="card card--front">
    <div class="brand">
      <span class="brand__square"></span>
      <span class="brand__name">Vexomari</span>
    </div>
    <div class="divider"></div>
    <div class="contact">
      <p class="contact__name">Jeroen Maas</p>
      <p class="contact__role">President</p>
      <p class="contact__address">Lindenhoutkade 42<br>3617KW Utrecht</p>
      <p class="contact__line">
        <svg viewBox="0 0 12 12"><path d="M2 1h2.5l1 3-1.5 1a6 6 0 0 0 3 3l1-1.5 3 1V10a1 1 0 0 1-1 1A9 9 0 0 1 1 2a1 1 0 0 1 1-1z"/></svg>
        +31 302849516
      </p>
      <p class="contact__line">
        <svg viewBox="0 0 12 12"><path d="M3 0h6a1 1 0 0 1 1 1v10a1 1 0 0 1-1 1H3a1 1 0 0 1-1-1V1a1 1 0 0 1 1-1zm0 1.5v8h6v-8z"/></svg>
        +31 6 58193074
      </p>
      <p class="contact__line">
        <svg viewBox="0 0 12 12"><path d="M3 0h6v3H3zM1 4h10v5H9v3H3V9H1zm3 4v3h4V8z"/></svg>
        +31 302849520
      </p>
      <p class="contact__line">
        <svg viewBox="0 0 12 12"><path d="M0 2h12v1L6 7 0 3zm0 2.2 6 4 6-4V10H0z"/></svg>
        jeroen@vexomari.example
      </p>
      <p class="contact__line">
        <svg viewBox="0 0 12 12"><circle cx="6" cy="6" r="6"/></svg>
        https://vexomari.example
      </p>
    </div>
  </section>
</body>
</html>
```